Corvalent Growth Partners in need of a business card design

We need an innovative business card designed for a new company in Alberta, Canada. We assist organizations in improving performance by providing coaching and mentorship on how to promote and achieve organizational excellence. We teach senior leaders and their staff on how to continually improve performance; assist them in making sure the organization is innovative, competitive, and customer focused; support them in making sure the culture of the organization is also healthy, inclusive, and sustainable; and they are economically, socially, and environmentally responsible. We will do this by staying true to our company values of respect, excellence, integrity and trust.

Attached is our newly designed logo.

The team thought that having an inspirational quote similar to this one below would be a good addition somewhere on the card.

"Autograph your work with excellence.''

Target Market(s)

Private and public sector organizations. Once that are interested in being a Top 100 employer.

Industry/Entity Type

Business

Font styles to use
Sans Serif

Requirements
Must have
• 1. The business card must be double-sided.
2. Person's name and title
3. Email address
4. Phone number
5. Website (corvalentgrowth.ca)
6. QR code
7. A quote somewhere on the front of the card: Autograph your work with excellence.
Nice to have

```html
<!DOCTYPE html>
<html lang="en">
<head>
<meta charset="utf-8">
<title>Corvalent Growth Partners – Business Card</title>
<link rel="stylesheet" href="https://fonts.googleapis.com/css2?family=Roboto:wght@300;400;500;700&display=swap">
<style>
  :root {
    --canvas: #e9e7e4;
    --card-top: #2b2a2a;
    --card-bottom: #0b0b0b;
    --white: #ffffff;
    --muted: #bdbdbd;
    --ink: #111111;
    --purple: #7a5bb0;
    --purple-deep: #4b3480;
    --blue: #2f8fcf;
    --blue-deep: #1c5f9e;
    --lime: #8cc63f;
    --lime-deep: #5f9a1e;
  }
  * { box-sizing: border-box; margin: 0; padding: 0; }
  html, body {
    width: 1200px; height: 913px; overflow: hidden;
    background: var(--canvas);
    font-family: "Roboto", Arial, sans-serif;
  }
  .canvas {
    position: relative; width: 1200px; height: 913px;
    display: flex; align-items: center; justify-content: center; gap: 40px;
  }
  .card {
    position: relative; width: 540px; height: 309px; overflow: hidden;
    border-radius: 4px;
    background: linear-gradient(160deg, var(--card-top) 0%, var(--card-bottom) 70%);
    box-shadow: 0 10px 28px rgba(0,0,0,.25);
  }

  /* Front */
  .front-brand {
    position: absolute; left: 0; right: 0; top: 118px;
    display: flex; align-items: center; justify-content: center; gap: 14px;
  }
  .brand-dot { width: 30px; height: 30px; border-radius: 50%; background: var(--lime); flex: none; }
  .brand-name {
    color: var(--white); font-weight: 500; font-size: 30px; line-height: 1.1;
    letter-spacing: .5px; white-space: nowrap;
  }
  .front-quote {
    position: absolute; left: 0; right: 0; bottom: 34px;
    text-align: center; color: var(--muted);
    font-weight: 300; font-size: 14px; letter-spacing: 1px;
  }

  /* Back */
  .back-brand {
    position: absolute; right: 24px; top: 24px;
    display: flex; align-items: center; gap: 10px;
  }
  .back-brand .brand-dot { width: 18px; height: 18px; }
  .back-brand .brand-name { font-size: 16px; }

  .qr-code {
    position: absolute; left: 26px; top: 22px; width: 72px; height: 72px;
    background: var(--white); border-radius: 3px;
  }

  .name-tab {
    position: absolute; left: 0; top: 112px; width: 230px; height: 64px;
    background: var(--white); border-radius: 0 32px 32px 0;
    padding: 12px 0 0 26px;
  }
  .person-name { color: var(--ink); font-weight: 700; font-size: 19px; white-space: nowrap; }
  .person-title { color: var(--ink); font-weight: 400; font-size: 12px; margin-top: 4px; }

  .contact-bar {
    position: absolute; left: 0; height: 30px;
    border-radius: 0 15px 15px 0;
    display: flex; align-items: center;
    color: var(--white); font-size: 13px; white-space: nowrap;
  }
  .contact-bar .icon-cell {
    width: 42px; height: 100%; margin-left: 118px;
    display: flex; align-items: center; justify-content: center;
  }
  .contact-bar svg { width: 16px; height: 16px; }
  .contact-bar .value { padding-left: 12px; }

  .bar-phone { top: 194px; width: 400px; background: linear-gradient(90deg, var(--purple-deep), var(--purple)); }
  .bar-email { top: 232px; width: 440px; background: linear-gradient(90deg, var(--blue-deep), var(--blue)); }
  .bar-web   { top: 270px; width: 480px; background: linear-gradient(90deg, var(--lime-deep), var(--lime)); }
</style>
</head>
<body>
<main class="canvas">
  <section class="card card-front" aria-label="Card front">
    <div class="front-brand">
      <span class="brand-dot"></span>
      <span class="brand-name">Corvalent Growth Partners</span>
    </div>
    <p class="front-quote">“Autograph your work with excellence.”</p>
  </section>

  <section class="card card-back" aria-label="Card back">
    <div class="qr-code" role="img" aria-label="QR code linking to corvalentgrowth.ca"></div>

    <div class="back-brand">
      <span class="brand-dot"></span>
      <span class="brand-name">Corvalent Growth Partners</span>
    </div>

    <div class="name-tab">
      <p class="person-name">Your Long Name</p>
      <p class="person-title">Titel</p>
    </div>

    <div class="contact-bar bar-phone">
      <span class="icon-cell">
        <svg viewBox="0 0 24 24" aria-hidden="true"><path fill="#fff" d="M6.6 10.8a15.1 15.1 0 0 0 6.6 6.6l2.2-2.2c.3-.3.7-.4 1-.2 1.1.4 2.3.6 3.6.6.6 0 1 .4 1 1V20c0 .6-.4 1-1 1A17 17 0 0 1 3 4c0-.6.4-1 1-1h3.5c.6 0 1 .4 1 1 0 1.3.2 2.5.6 3.6.1.3 0 .7-.2 1z"/></svg>
      </span>
      <span class="value">00.00.00.0000</span>
    </div>

    <div class="contact-bar bar-email">
      <span class="icon-cell">
        <svg viewBox="0 0 24 24" aria-hidden="true"><rect x="2" y="5" width="20" height="14" rx="1" fill="#fff"/><path d="M2 6l10 7 10-7" fill="none" stroke="#1c5f9e" stroke-width="1.6"/></svg>
      </span>
      <span class="value">yourname@corvalentgrowth.ca</span>
    </div>

    <div class="contact-bar bar-web">
      <span class="icon-cell">
        <svg viewBox="0 0 24 24" aria-hidden="true"><g fill="none" stroke="#fff" stroke-width="1.8"><circle cx="12" cy="12" r="9"/><ellipse cx="12" cy="12" rx="4" ry="9"/><path d="M3 12h18"/></g></svg>
      </span>
      <span class="value">www.corvalentgrowth.ca</span>
    </div>
  </section>
</main>
</body>
</html>
```